FREE SOCIAL SECURITY DISABILITY CLAIM EVALUATION - Ad Banners & Email Marketing Creatives

Looking for design of ad banners and email creative for my Social Security Disability Insurance Benefits Application, Denial, & Appeals Help website. Call to action based email focused on conveying brand, messaging of "Are you out of work due to a disability? You may qualify for up to $2,642 per month in Social Security Disability benefits!" and "ACT NOW: Check Your Eligibility" Call to action of 'Get Your FREE Evaluation' or 'Fast, FREE, No Obligation Evaluation' or 'Confirm My Eligibility Now!' or 'Start My FREE Evaluation' or 'Confirm My Eligibility Now!'. Can use any messaging and images from the current website:
https://harborline-intakes.com/

Please focus on imaging that matches the site. The final Ad Banners must be delivered in both JPG and PSD file formats. Ad Banners must follow QRV standards.

We need Ad Banners in the following sizes.
728x90
300x250
336x280
160x600
1200x628
600x600
1080x1080
Email

Target Market(s)
People in the US between the ages 48-63 looking for Social Security Disability Insurance Benefits Application, Denial, & Appeals Help. Get connected to a local Social Security Disability legal representative for a free, no-obligation evaluation. Find out if you are eligible to receive financial compensation for as much as $2,642 a month!

Should not be cookie cutter. Stick to simple yet official looking.

The final Email creative must be done in responsive HTML as well as text for easy use and include Email Opt Out link etc.

Target Market(s)

Americans that are between the ages 48-63 that have a physical condition that prevents them from working. Many times the physical condition is a result of an injury.

Coding

Coded - Design and coding required

Font styles to use
Sans Serif

Requirements
Must have
• A strong call to action.
Should not have
• No photos of people in wheelchairs.

```html
<!DOCTYPE html>
<html lang="en">
<head>
<meta charset="utf-8">
<title>Free Social Security Disability Claim Evaluation – Ad Banner Set</title>
<link rel="stylesheet" href="https://fonts.googleapis.com/css2?family=Roboto+Condensed:ital,wght@0,400;0,700;1,700&display=swap">
<style>
:root{
  --navy:#0d3473;
  --navy-deep:#08245a;
  --sky:#2ea3e6;
  --seal-bg:#8fc3e3;
  --ink:#1c2f55;
  --pale:#e7f2fb;
  --label:#9aa3ad;
  --white:#ffffff;
}
*{box-sizing:border-box;margin:0;padding:0}
html,body{width:1200px;height:2442px;overflow:hidden;background:var(--white)}
body{position:relative;font-family:"Roboto Condensed",sans-serif;color:var(--ink)}
.abs{position:absolute}
.banner{position:absolute;border:1.5px solid var(--navy);background:var(--white);overflow:hidden}
.icon{position:absolute;display:block;filter:drop-shadow(0 3px 3px rgba(0,0,0,.35))}
.sky{color:var(--sky)}
.navy{color:var(--navy)}
b{font-weight:700}
.center{text-align:center;left:0;right:0}

/* size list */
.size-list{left:139px;top:134px;font:italic 700 23px/29.5px "Roboto Condensed",sans-serif;color:var(--label)}

/* 728x90 */
.b728{left:388px;top:72px;width:578px;height:73px}
.b728 .hl{left:20px;top:2px;font-size:21px;line-height:23px;font-weight:400}
.b728 .hl .big{font-size:25px;font-weight:700;color:var(--navy)}
.b728 .fine{left:19px;top:56px;font-size:11px;color:var(--navy)}
.b728 .cta{right:0;top:0;width:160px;height:73px;background:var(--navy);clip-path:polygon(14% 0,100% 0,100% 100%,0 100%);color:var(--white);text-align:center;padding-left:28px}
.b728 .cta .t{font-size:18px;line-height:21px;font-weight:700;margin-top:6px}
.b728 .cta .u{font-size:8px;margin-top:3px}

/* 300x250 */
.b300{left:388px;top:173px;width:239px;height:200px}
.b300 .hl{top:50px;font-size:24px;line-height:27px;color:var(--sky)}
.b300 .hl .big{font-size:29px;font-weight:700;color:var(--navy)}
.b300 .fine{top:107px;font-size:11.5px;line-height:16px;color:var(--ink)}
.b300 .band{left:0;right:0;bottom:0;height:38px;background:var(--navy);color:var(--white);text-align:center}
.b300 .band .t{font-size:17px;font-weight:700;margin-top:2px}
.b300 .band .u{font-size:11px}

/* 336x280 */
.b336{left:662px;top:173px;width:267px;height:223px}
.b336 .top{left:0;right:0;top:0;height:78px;background:linear-gradient(180deg,var(--pale),#cfe5f5)}
.b336 .hl{top:2px;font-size:25px;line-height:27px;color:var(--navy)}
.b336 .hl b{font-size:29px}
.b336 .fine{top:124px;font-size:12px;line-height:16px;color:var(--ink)}
.b336 .band{left:0;right:0;bottom:0;height:44px;background:var(--navy);color:var(--white);text-align:center}
.b336 .band .t{font-size:18px;font-weight:700;margin-top:3px}
.b336 .band .u{font-size:12px}

/* 160x600 */
.b160{left:1012px;top:72px;width:128px;height:476px}
.b160 .hl{top:12px;font-size:21px;line-height:24px;font-weight:700;color:var(--sky)}
.b160 .hl .n{color:var(--navy)}
.b160 .fine{top:240px;font-size:15px;line-height:20px;color:var(--ink)}
.b160 .band{left:0;right:0;bottom:0;height:112px;background:var(--navy);color:var(--white);text-align:center;font-weight:700}
.b160 .band .t{font-size:18px;margin-top:9px}
.b160 .band .f{font-size:26px;line-height:27px}
.b160 .band .u{font-size:8px;font-weight:400;margin-top:5px}

/* shared header for large pieces */
.claim-title{position:absolute;display:block;overflow:visible}
.claim-title text{font-family:"Roboto Condensed",sans-serif;font-weight:400;fill:var(--navy)}
.claim-sub{color:var(--navy);white-space:nowrap}
.seal{position:absolute;background:var(--seal-bg);display:flex;flex-direction:column;align-items:center;justify-content:center;gap:6px;color:var(--navy);font-size:15px;font-weight:700}
.seal i{display:block;width:44px;height:44px;border-radius:50%;background:var(--white);opacity:.6}
.btn{position:absolute;background:linear-gradient(180deg,#1b4d9a,var(--navy-deep));border:3px solid var(--white);border-radius:14px;box-shadow:0 4px 8px rgba(0,0,0,.35);color:var(--white);font-weight:700;text-align:center;white-space:nowrap}

/* 1200x628 */
.b1200{left:35px;top:425px;width:951px;height:499px;
  background:
   radial-gradient(ellipse 55% 40% at 80% 85%,rgba(255,255,255,.85),transparent 70%),
   linear-gradient(160deg,#eef6fd 0%,#b9dcf3 40%,#5fb2e6 75%,#2a86d2 100%)}
.b1200 .claim-title{left:137px;top:25px}
.b1200 .sub{left:137px;width:679px;top:64px;font-size:21px;text-align:center}
.b1200 .hl{top:258px;font-size:56px;font-weight:700;color:var(--navy);text-shadow:0 2px 2px rgba(255,255,255,.8);white-space:nowrap}
.b1200 .qual{left:40px;top:338px;width:360px;text-align:center;font-size:28px;line-height:34px;color:var(--navy)}
.b1200 .btn{left:401px;top:344px;width:481px;height:78px;font-size:45px;line-height:72px}
.b1200 .url{left:401px;top:430px;width:481px;text-align:center;font-size:31px;color:var(--navy)}

/* 600x600 */
.b600{left:35px;top:946px;width:476px;height:476px}
.b600 .claim-title{left:24px;top:9px}
.b600 .sub{top:35px;font-size:13.5px;left:0;right:0;text-align:center}
.b600 .hl{top:158px;font-size:52px;line-height:58px;font-weight:700;color:var(--sky)}
.b600 .hl .big{font-size:58px;color:var(--navy)}
.b600 .qual{top:288px;font-size:24px;line-height:30px;color:var(--navy)}
.b600 .btn{left:37px;top:360px;width:390px;height:63px;font-size:37px;line-height:56px}
.b600 .url{top:440px;font-size:26px;color:var(--navy)}

/* 1080x1080 */
.b1080{left:158px;top:1478px;width:856px;height:856px;
  background:linear-gradient(180deg,var(--white) 0%,var(--white) 22%,#d6e9f7 50%,#6fb7e6 78%,#2f7fcc 100%)}
.b1080 .photo{left:526px;top:466px;width:330px;height:390px;
  background:radial-gradient(ellipse 70% 60% at 55% 55%,rgba(13,52,115,.85),rgba(47,127,204,.2) 75%,transparent 90%)}
.b1080 .claim-title{left:136px;top:12px}
.b1080 .sub{left:137px;top:53px;font-size:21px}
.b1080 .hl{left:0;width:460px;top:148px;text-align:right;font-size:70px;line-height:84px;font-weight:700;color:var(--sky)}
.b1080 .hl .big{font-size:78px;color:var(--navy)}
.b1080 .qual{left:80px;top:424px;font-size:37px;line-height:48px;color:var(--navy)}
.b1080 .btn{left:64px;top:592px;width:482px;height:78px;font-size:46px;line-height:70px}
.b1080 .legal{left:28px;top:690px;width:508px;font-size:11.2px;line-height:15.4px;text-align:justify;color:var(--navy)}
.b1080 .url{left:80px;top:806px;font-size:32px;color:var(--navy)}
</style>
</head>
<body>

<svg width="0" height="0" style="position:absolute" aria-hidden="true">
  <defs>
    <radialGradient id="disc" cx="40%" cy="35%" r="70%">
      <stop offset="0" stop-color="#2f62ad"/>
      <stop offset="1" stop-color="#0a2a62"/>
    </radialGradient>
    <symbol id="ic-wheelchair" viewBox="0 0 100 100">
      <circle cx="50" cy="50" r="47" fill="url(#disc)" stroke="#fff" stroke-width="3"/>
      <circle cx="42" cy="22" r="7" fill="#f2f2f2"/>
      <path d="M40 32 L42 56 L64 56 L72 76" fill="none" stroke="#f2f2f2" stroke-width="8" stroke-linecap="round" stroke-linejoin="round"/>
      <path d="M41 44 L58 44" stroke="#f2f2f2" stroke-width="7" stroke-linecap="round"/>
      <path d="M32 46 A20 20 0 1 0 62 70" fill="none" stroke="#f2f2f2" stroke-width="7" stroke-linecap="round"/>
    </symbol>
    <symbol id="ic-head" viewBox="0 0 100 100">
      <circle cx="50" cy="50" r="47" fill="url(#disc)" stroke="#fff" stroke-width="3"/>
      <path d="M30 76 L30 62 C18 52 20 26 44 22 C64 19 76 32 74 48 L80 58 L74 60 L74 68 C74 72 70 73 64 72 L62 78" fill="none" stroke="#f2f2f2" stroke-width="4" stroke-linejoin="round"/>
      <path d="M32 46 C30 32 44 26 56 28 C68 30 70 42 64 48 C58 54 40 54 32 46Z" fill="#f2f2f2"/>
    </symbol>
    <symbol id="ic-hands" viewBox="0 0 100 100">
      <circle cx="50" cy="50" r="47" fill="url(#disc)" stroke="#fff" stroke-width="3"/>
      <path d="M16 40 L34 28 L44 34 L40 48 L26 56 Z" fill="#f2f2f2"/>
      <circle cx="38" cy="54" r="7" fill="none" stroke="#f2f2f2" stroke-width="4"/>
      <path d="M54 40 L72 34 L84 48 L78 70 L62 74 L54 62 L64 56 L56 48 Z" fill="#f2f2f2"/>
      <circle cx="68" cy="56" r="5" fill="url(#disc)"/>
    </symbol>
    <symbol id="ic-cane" viewBox="0 0 100 100">
      <circle cx="50" cy="50" r="47" fill="url(#disc)" stroke="#fff" stroke-width="3"/>
      <circle cx="44" cy="20" r="7" fill="#f2f2f2"/>
      <path d="M44 30 L40 54 L34 80 M40 54 L52 80 M44 34 L56 48 L62 52 M44 34 L34 50" fill="none" stroke="#f2f2f2" stroke-width="8" stroke-linecap="round" stroke-linejoin="round"/>
      <path d="M60 50 L82 84" stroke="#f2f2f2" stroke-width="3" stroke-linecap="round"/>
    </symbol>
  </defs>
</svg>

<div class="abs size-list">728x90<br>300x250<br>336x280<br>160x600<br>1200x628<br>600x600<br>1080x1080</div>

<!-- 728x90 leaderboard -->
<section class="banner b728">
  <div class="abs hl sky">Are you out of work<br>due to <span class="big">a disability?</span></div>
  <svg class="icon" style="left:221px;top:8px" width="41" height="41"><use href="#ic-wheelchair"/></svg>
  <svg class="icon" style="left:273px;top:8px" width="41" height="41"><use href="#ic-head"/></svg>
  <svg class="icon" style="left:325px;top:8px" width="41" height="41"><use href="#ic-hands"/></svg>
  <svg class="icon" style="left:377px;top:8px" width="41" height="41"><use href="#ic-cane"/></svg>
  <div class="abs fine">You may qualify for up to <b>$2,642 per month</b> in Social Security Disability benefits!</div>
  <div class="abs cta"><div class="t">Get Your FREE<br>Evaluation</div><div class="u">www.harborline-intakes.com</div></div>
</section>

<!-- 300x250 medium rectangle -->
<section class="banner b300">
  <svg class="icon" style="left:14px;top:7px" width="42" height="42"><use href="#ic-wheelchair"/></svg>
  <svg class="icon" style="left:66px;top:7px" width="42" height="42"><use href="#ic-head"/></svg>
  <svg class="icon" style="left:118px;top:7px" width="42" height="42"><use href="#ic-hands"/></svg>
  <svg class="icon" style="left:170px;top:7px" width="42" height="42"><use href="#ic-cane"/></svg>
  <div class="abs center hl">Are you out of work<br>due to <span class="big">a disability?</span></div>
  <div class="abs center fine">You may qualify for up to<br><b>$2,642 per month</b> in<br>Social Security Disability benefits!</div>
  <div class="abs band"><div class="t">Get Your Free Evaluation</div><div class="u">www.harborline-intakes.com</div></div>
</section>

<!-- 336x280 large rectangle -->
<section class="banner b336">
  <div class="abs top"></div>
  <svg class="abs" style="left:0;top:56px" width="267" height="30" viewBox="0 0 267 30" aria-hidden="true"><path d="M0 30 C60 0 160 0 267 14 L267 30 Z" fill="#fff"/></svg>
  <div class="abs center hl">Are you out of work<br>due to a <b>disability?</b></div>
  <svg class="icon" style="left:17px;top:69px" width="50" height="50"><use href="#ic-wheelchair"/></svg>
  <svg class="icon" style="left:78px;top:69px" width="50" height="50"><use href="#ic-head"/></svg>
  <svg class="icon" style="left:139px;top:69px" width="50" height="50"><use href="#ic-hands"/></svg>
  <svg class="icon" style="left:200px;top:69px" width="50" height="50"><use href="#ic-cane"/></svg>
  <div class="abs center fine">You may qualify for up to<br><b>$2,642 per month</b> in<br>Social Security Disability benefits!</div>
  <div class="abs band"><div class="t">Get Your Free Evaluation</div><div class="u">www.harborline-intakes.com</div></div>
</section>

<!-- 160x600 skyscraper -->
<section class="banner b160">
  <div class="abs center hl">Are you out<br>of work<br><span class="n">due to a<br>disability?</span></div>
  <svg class="icon" style="left:8px;top:123px" width="52" height="52"><use href="#ic-wheelchair"/></svg>
  <svg class="icon" style="left:68px;top:123px" width="52" height="52"><use href="#ic-head"/></svg>
  <svg class="icon" style="left:8px;top:180px" width="52" height="52"><use href="#ic-hands"/></svg>
  <svg class="icon" style="left:68px;top:180px" width="52" height="52"><use href="#ic-cane"/></svg>
  <div class="abs center fine">You may qualify<br>for up to<br><b>$2,642</b><br><b>per month</b> in<br>Social Security<br>Disability benefits!</div>
  <div class="abs band"><div class="t">Get Your</div><div class="f">FREE</div><div>Evaluation</div><div class="u">www.harborline-intakes.com</div></div>
</section>

<!-- 1200x628 social -->
<section class="banner b1200">
  <div class="seal" style="left:12px;top:10px;width:110px;height:100px"><i></i>Harborline</div>
  <div class="seal" style="right:10px;top:10px;width:110px;height:100px"><i></i>Harborline</div>
  <svg class="claim-title" width="679" height="36" viewBox="0 0 679 36"><text x="0" y="30" font-size="34" textLength="679" lengthAdjust="spacingAndGlyphs">FREE SOCIAL SECURITY DISABILITY CLAIM EVALUATION</text></svg>
  <div class="abs claim-sub sub">Social Security Disability Insurance Benefits Application, Denial, &amp; Appeals Help.</div>
  <svg class="icon" style="left:149px;top:99px" width="146" height="146"><use href="#ic-wheelchair"/></svg>
  <svg class="icon" style="left:320px;top:99px" width="146" height="146"><use href="#ic-head"/></svg>
  <svg class="icon" style="left:492px;top:99px" width="146" height="146"><use href="#ic-hands"/></svg>
  <svg class="icon" style="left:667px;top:99px" width="146" height="146"><use href="#ic-cane"/></svg>
  <div class="abs center hl" style="text-align:center">Are you out of work due to a disability?</div>
  <div class="abs qual">You may qualify for up to<br><b>$2,642 per month</b> in Social<br>Security Disability benefits!</div>
  <div class="btn">Get Your Free Evaluation</div>
  <div class="abs url">www.harborline-intakes.com</div>
</section>

<!-- 600x600 square -->
<section class="banner b600">
  <svg class="claim-title" width="436" height="24" viewBox="0 0 436 24"><text x="0" y="20" font-size="22" textLength="436" lengthAdjust="spacingAndGlyphs">FREE SOCIAL SECURITY DISABILITY CLAIM EVALUATION</text></svg>
  <div class="abs claim-sub sub">Social Security Disability Insurance Benefits Application, Denial, &amp; Appeals Help.</div>
  <svg class="icon" style="left:21px;top:55px" width="92" height="92"><use href="#ic-wheelchair"/></svg>
  <svg class="icon" style="left:128px;top:55px" width="92" height="92"><use href="#ic-head"/></svg>
  <svg class="icon" style="left:238px;top:55px" width="92" height="92"><use href="#ic-hands"/></svg>
  <svg class="icon" style="left:350px;top:55px" width="92" height="92"><use href="#ic-cane"/></svg>
  <div class="abs center hl" style="text-align:center">Are you out of work<br>due to <span class="big">a disability?</span></div>
  <div class="abs center qual" style="text-align:center">You may qualify for up to <b>$2,642 per month</b><br>in Social Security Disability benefits!</div>
  <div class="btn">Get Your Free Evaluation</div>
  <div class="abs center url" style="text-align:center">www.harborline-intakes.com</div>
</section>

<!-- 1080x1080 square -->
<section class="banner b1080">
  <div class="abs photo" role="img" aria-label="Photo of a man in a suit seated, seen from behind, in soft blue light"></div>
  <div class="seal" style="left:9px;top:10px;width:111px;height:100px"><i></i>Harborline</div>
  <svg class="claim-title" width="677" height="36" viewBox="0 0 677 36"><text x="0" y="30" font-size="34" textLength="677" lengthAdjust="spacingAndGlyphs">FREE SOCIAL SECURITY DISABILITY CLAIM EVALUATION</text></svg>
  <div class="abs claim-sub sub">Social Security Disability Insurance Benefits Application, Denial, &amp; Appeals Help.</div>
  <div class="abs hl">Are you out of<br>work due to<br><span class="big">a disability?</span></div>
  <svg class="icon" style="left:496px;top:139px" width="136" height="136"><use href="#ic-wheelchair"/></svg>
  <svg class="icon" style="left:653px;top:139px" width="136" height="136"><use href="#ic-head"/></svg>
  <svg class="icon" style="left:500px;top:288px" width="136" height="136"><use href="#ic-hands"/></svg>
  <svg class="icon" style="left:661px;top:288px" width="136" height="136"><use href="#ic-cane"/></svg>
  <div class="abs qual">You may qualify for up to<br><b>$2,642 per month</b> in Social<br>Security Disability benefits!</div>
  <div class="btn">Get Your Free Evaluation</div>
  <p class="abs legal">Important Note About Applying or Re-Applying For Disability Benefits: Utilizing a Social Security Disability attorney or advocate may improve your chances of initial approval, get your approval processed more quickly and in many cases increase the amount of benefits you are awarded. There are no upfront expenses to you for the evaluation, filing or appeal process. To get immediate assistance from one of our attorneys or advocates, please fill out the FREE Evaluation Form Above. This website is not affiliated with the Social Security Administration ("SSA") or any state or federal agency. If you choose to apply on your own without representation, you may do so at no cost on the SSA website.</p>
  <div class="abs url">www.harborline-intakes.com</div>
</section>

</body>
</html>
```